Velno Recycling needs a new web design

We need a new web design for our company based in Austin, TX. We resell and recycling electronics such as laptops, computer components, Tovlets, Brunos, etc. Since our inception over ten years ago, we’ve become one of the premier electronics recycling and remarketing companies in Austin, Texas.

```html
<!DOCTYPE html>
<html lang="en">
<head>
<meta charset="utf-8">
<title>Velno Recycling</title>
<link href="https://fonts.googleapis.com/css2?family=Jost:wght@300;400;500;600;700&display=swap" rel="stylesheet">
<style>
:root{
  --stage:#e4e9ed;
  --blue:#1a74c4;
  --navy:#133a73;
  --ink:#3a3f47;
  --muted:#7b828c;
  --dark:#2c2d30;
  --light:#f3f5f8;
  --white:#ffffff;
  --line:#d8dde3;
}
*{box-sizing:border-box;margin:0;padding:0}
html,body{width:1200px;height:3711px;overflow:hidden}
body{background:var(--stage);font-family:"Jost",sans-serif;color:var(--ink)}
.page{position:absolute;left:40px;top:181px;width:1120px;background:var(--white);box-shadow:0 6px 30px rgba(0,0,0,.08)}
section,footer{position:relative;overflow:hidden}
.btn{display:inline-block;background:var(--blue);color:var(--white);font-size:14px;font-weight:500;padding:10px 22px;border-radius:2px}
.section-title{position:absolute;left:0;right:0;text-align:center;font-size:28px;font-weight:300;letter-spacing:.5px}
.section-title b{font-weight:600}

/* hero */
.hero{height:528px}
.hero-photo{position:absolute;inset:0;background:linear-gradient(180deg,#5d7fa6 0%,#8fb0cf 45%,#c9d7e3 80%,#dfe6ec 100%)}
.site-header{position:absolute;left:8px;right:8px;top:6px;height:76px;background:var(--white);display:flex;align-items:center;padding:0 32px}
.brand{display:flex;align-items:center;gap:12px;font-size:24px;font-weight:600;color:var(--navy)}
.brand-dot{width:34px;height:34px;border-radius:50%;border:3px solid var(--blue)}
.nav{display:flex;gap:30px;margin-left:auto;font-size:12px;font-weight:500;letter-spacing:1px;text-transform:uppercase;color:var(--ink)}
.nav .active{color:var(--blue);border-bottom:2px solid var(--blue);padding-bottom:4px}
.header-cta{margin-left:40px}
.hero-copy{position:absolute;left:147px;top:220px;width:520px;color:var(--white);font-size:26px;line-height:1.3;font-weight:400}
.hero-copy b{font-weight:600}
.hero-copy .btn{margin-top:26px}

/* intro */
.intro{height:270px;text-align:center}
.emblem{position:absolute;left:511px;top:-49px;width:98px;height:98px;border-radius:50%;background:var(--white);border:4px solid var(--navy);box-shadow:0 0 0 6px var(--white)}
.intro p{position:absolute;left:250px;right:250px;top:62px;font-size:16px;line-height:1.55;color:var(--muted)}
.discover{position:absolute;left:0;right:0;top:176px;font-size:13px;color:var(--blue)}
.discover span{border-bottom:1px solid var(--blue);padding-bottom:3px}

/* services */
.services{height:347px;color:var(--white)}
.services-photo,.testimonial-photo{position:absolute;inset:0;background:linear-gradient(135deg,#3a3b3e,#242527 60%,#303134)}
.services .section-title{top:56px}
.divider{position:absolute;left:560px;top:120px;width:1px;height:190px;background:rgba(255,255,255,.25)}
.service{position:absolute;top:112px;width:420px;text-align:center}
.service.left{left:90px}
.service.right{left:610px}
.service svg{display:block;margin:0 auto 6px}
.service h3{font-size:18px;font-weight:500;color:var(--blue);line-height:1.1}
.service h4{font-size:11px;font-weight:500;color:#d9dde2;margin-bottom:12px}
.service p{font-size:13px;line-height:1.5;color:#c9cdd2}
.service .btn{margin-top:14px;font-size:12px;padding:8px 18px}
.service.left .btn{background:transparent;color:#8a9bb0;border:1px solid rgba(255,255,255,.2)}

/* items */
.items{height:660px;background:var(--light)}
.items .section-title{top:78px;color:var(--ink)}
.items .section-title b{color:var(--blue)}
.hub{position:absolute;left:412px;top:211px;width:296px;height:296px;border-radius:50%;background:var(--navy);color:var(--white);display:flex;align-items:center;justify-content:center;text-align:center;font-size:26px;font-weight:300;line-height:1.25}
.hub b{font-weight:600}
.item-icon{position:absolute;width:74px;height:74px;border-radius:50%;background:var(--blue);border:4px solid var(--white);display:flex;align-items:center;justify-content:center}
.item{position:absolute;width:250px;font-size:12px;line-height:1.45;color:var(--muted)}
.item h3{font-size:16px;font-weight:600;color:var(--blue);margin-bottom:4px}
.item.l{left:143px;text-align:right}
.item.r{left:740px}
.items .btn{position:absolute;left:484px;top:566px;font-size:12px;padding:8px 22px}

/* testimonial */
.testimonial{height:455px;color:var(--white);text-align:center}
.quote-mark{position:absolute;left:0;right:0;top:70px;font-size:70px;line-height:1;color:var(--blue);font-weight:700}
.testimonial blockquote{position:absolute;left:250px;right:250px;top:128px;font-size:17px;line-height:1.55;font-weight:300;color:#dfe2e6}
.avatar{position:absolute;left:530px;top:270px;width:60px;height:60px;border-radius:50%;background:#8d8f94;border:3px solid var(--white)}
.person{position:absolute;left:0;right:0;top:342px;font-size:14px;font-weight:500}
.person small{display:block;font-size:11px;font-weight:400;color:#a9adb3}

/* certificates */
.certificates{height:313px}
.certificates .section-title{top:72px;color:var(--ink)}
.badges{position:absolute;left:108px;right:108px;top:123px;display:flex;justify-content:space-between}
.badge{width:110px;height:110px;border:1px solid var(--line);display:flex;align-items:center;justify-content:center;background:var(--white)}
.badge i{display:block;width:74px;height:74px;border-radius:50%}

/* contact */
.contact{height:356px;background:var(--light)}
.contact-copy{position:absolute;left:147px;top:100px;width:330px}
.contact-copy h2{font-size:21px;font-weight:500;line-height:1.3;color:var(--dark)}
.contact-copy p{font-size:12px;line-height:1.5;color:var(--muted);margin-top:12px}
.contact-form{position:absolute;left:571px;top:56px;width:402px;display:grid;grid-template-columns:1fr 1fr;gap:12px 12px}
.field{height:32px;background:var(--white);border:1px solid var(--line);font-size:11px;color:var(--muted);padding:8px 10px}
.field.wide{grid-column:span 2}
.field.message{height:96px}
.send{position:absolute;left:944px;top:318px;width:30px;height:30px;border-radius:50%;background:var(--blue);display:flex;align-items:center;justify-content:center}

/* map footer */
.find-us{height:359px}
.map{position:absolute;inset:0;background:linear-gradient(180deg,#eef0f2,#e4e7ea)}
.pin{position:absolute;left:820px;top:160px}
.find-card{position:absolute;left:147px;top:0;width:261px;height:359px;background:var(--blue);color:var(--white);padding:40px 28px}
.find-card h2{font-size:19px;font-weight:500;margin-bottom:12px}
.find-card p{font-size:11px;line-height:1.55;color:#dce9f6}
.find-card .phones{margin-top:12px}
.find-card .phones strong{font-weight:600;color:var(--white)}
.find-card .mail{margin-top:12px;text-decoration:underline}
.socials{position:absolute;left:28px;bottom:30px;display:flex;gap:8px}
.socials i{display:block;width:26px;height:26px;background:rgba(255,255,255,.25)}
.bottom-bar{height:61px;background:var(--white);display:flex;align-items:center;padding:0 32px 0 36px;font-size:11px;color:var(--muted)}
.bottom-links{margin-left:auto;margin-right:40px}
.to-top{width:20px;height:20px;border-radius:50%;background:var(--blue);display:flex;align-items:center;justify-content:center}
</style>
</head>
<body>
<div class="page">

  <section class="hero">
    <div class="hero-photo" role="img" aria-label="Photo of a tree shaped like a recycling loop under a cloudy blue sky"></div>
    <header class="site-header">
      <div class="brand"><span class="brand-dot"></span>Velno Recycling</div>
      <nav class="nav">
        <span class="active">Home</span><span>About</span><span>Services</span><span>Items Accepted</span><span>Testimonials</span><span>Contact Us</span>
      </nav>
      <span class="btn header-cta">Schedule a Pickup</span>
    </header>
    <div class="hero-copy">
      We <b>Resell</b> and <b>Recycling</b> Electronics such as <b>Laptops, Computer Components, Tovlets, Brunos,</b> etc...
      <br><span class="btn">Contact Us</span>
    </div>
  </section>

  <section class="intro">
    <div class="emblem"></div>
    <p>What most people do not realize is electronic waste represents 2% of America's trash in landfills, but it equals 70% of overall toxic waste. Used computer equipment is a rapidly growing source of waste across the country. Only 12.5% of electronic waste is currently recycled in the US...</p>
    <div class="discover"><span>Discover More &rarr;</span></div>
  </section>

  <section class="services">
    <div class="services-photo" role="img" aria-label="Dark photo of circuit boards and electronic parts"></div>
    <h2 class="section-title">--- Recycling <b>Services</b> ---</h2>
    <div class="divider"></div>
    <div class="service left">
      <svg width="34" height="34" viewBox="0 0 34 34" fill="none" stroke="#1a74c4" stroke-width="3"><path d="M8 22 A11 11 0 0 1 17 6"/><path d="M17 6 l-4 -2 M17 6 l-3 4"/><path d="M26 12 A11 11 0 0 1 22 27"/><path d="M22 27 l1 -5 M22 27 l-4 -1"/><path d="M18 28 A11 11 0 0 1 7 24"/></svg>
      <h3>Electronic Recycling</h3>
      <h4>Environmentally Friendly</h4>
      <p>At Velno Recycling, we strive to keep the environment clean through our wide range of services. Our E-Waste Recycling services were designed to simplify the recycling process for residents in the Austin area. Contact us today and see how you can contribute to making the world a cleaner place.</p>
      <span class="btn">Schedule a Pickup</span>
    </div>
    <div class="service right">
      <svg width="40" height="34" viewBox="0 0 40 34" fill="#1a74c4"><rect x="2" y="8" width="22" height="16"/><path d="M25 13h8l5 6v5H25z"/><circle cx="10" cy="27" r="4"/><circle cx="31" cy="27" r="4"/></svg>
      <h3>Recycling Pickup</h3>
      <h4>We Come To You</h4>
      <p>At Velno Recycling, we go out of our way to make sure your recycling process is made easy as possible. Our Recycling Pickup service is designed to simplify all of your recycling needs. Take a look at all the services we offer and get in touch to see how you can assist the process today!</p>
      <span class="btn">Schedule a Pickup</span>
    </div>
  </section>

  <section class="items">
    <h2 class="section-title">--- Items <b>Accepted</b> ---</h2>
    <div class="hub"><div>A Full <b>Service</b><br>Electronic <b>Recycling</b><br>Company</div></div>
    <div class="item-icon" style="left:414px;top:230px"><svg width="34" height="26" viewBox="0 0 34 26" fill="none" stroke="#fff" stroke-width="2.5"><rect x="5" y="3" width="24" height="15"/><path d="M1 22h32"/></svg></div>
    <div class="item-icon" style="left:632px;top:230px"><svg width="30" height="30" viewBox="0 0 30 30" fill="none" stroke="#fff" stroke-width="2.5"><rect x="7" y="7" width="16" height="16"/><path d="M11 2v5M19 2v5M11 23v5M19 23v5M2 11h5M2 19h5M23 11h5M23 19h5"/></svg></div>
    <div class="item-icon" style="left:414px;top:427px"><svg width="22" height="32" viewBox="0 0 22 32" fill="none" stroke="#fff" stroke-width="2.5"><rect x="2" y="2" width="18" height="28" rx="2"/><circle cx="11" cy="25" r="1.2" fill="#fff"/></svg></div>
    <div class="item-icon" style="left:632px;top:427px"><svg width="32" height="30" viewBox="0 0 32 30" fill="none" stroke="#fff" stroke-width="2.5"><rect x="2" y="2" width="28" height="18" rx="1"/><path d="M16 20v6M9 28h14"/></svg></div>
    <div class="item l" style="top:225px"><h3>Laptops</h3>Sed ut perspiciatis unde omnis iste natus error sit voluptatem accusantium doloremque laudantium</div>
    <div class="item r" style="top:225px"><h3>Computer Components</h3>Sed ut perspiciatis unde omnis iste natus error sit voluptatem accusantium doloremque laudantium</div>
    <div class="item l" style="top:420px"><h3>Tovlets</h3>Sed ut perspiciatis unde omnis iste natus error sit voluptatem accusantium doloremque laudantium</div>
    <div class="item r" style="top:420px"><h3>Brunos System</h3>Sed ut perspiciatis unde omnis iste natus error sit voluptatem accusantium doloremque laudantium</div>
    <span class="btn">Explore More</span>
  </section>

  <section class="testimonial">
    <div class="testimonial-photo" role="img" aria-label="Dark photo of a workbench with electronics repair tools"></div>
    <div class="quote-mark">&ldquo;</div>
    <blockquote>Lorem ipsum dolor sit amet, consectetur adipiscing elit. Suspendisse eleifend id metus id fringilla. Phasellus euismod commodo felis, sit amet egestas dui euismod vitae. Aenean venenatis malesuada nisi sit amet hac can are amet hendrerit variations of passages.</blockquote>
    <div class="avatar" role="img" aria-label="Customer portrait"></div>
    <div class="person">Marlon Pettit<small>Founder, CEO</small></div>
  </section>

  <section class="certificates">
    <h2 class="section-title">--- Certificates ---</h2>
    <div class="badges">
      <div class="badge"><i style="background:#1f4f9a"></i></div>
      <div class="badge"><i style="background:#2a6db4"></i></div>
      <div class="badge"><i style="background:#3f7f4a"></i></div>
      <div class="badge"><i style="background:#5aa541"></i></div>
      <div class="badge"><i style="background:#2e7b52;border-radius:4px"></i></div>
      <div class="badge"><i style="background:#1c5ca8"></i></div>
      <div class="badge"><i style="background:#1f4f9a"></i></div>
    </div>
  </section>

  <section class="contact">
    <div class="contact-copy">
      <h2>Interested in helping to make the world a greener place?</h2>
      <p>Get in touch with Velno Recycling, and learn more about the wide range of recycling services and facilities that are at your disposal!</p>
    </div>
    <div class="contact-form">
      <div class="field">Your Name</div>
      <div class="field">Email</div>
      <div class="field">Phone</div>
      <div class="field">Subject</div>
      <div class="field wide">Address</div>
      <div class="field wide message">Message</div>
    </div>
    <div class="send"><svg width="12" height="12" viewBox="0 0 12 12" fill="#fff"><path d="M1 1l10 5-10 5 2-5z"/></svg></div>
  </section>

  <footer class="find-us">
    <div class="map" role="img" aria-label="Road map of the Austin, Texas area"></div>
    <svg class="pin" width="24" height="34" viewBox="0 0 24 34"><path d="M12 0a12 12 0 0 1 12 12c0 9-12 22-12 22S0 21 0 12A12 12 0 0 1 12 0z" fill="#1a74c4"/><circle cx="12" cy="12" r="4.5" fill="#fff"/></svg>
    <div class="find-card">
      <h2>How to Find Us</h2>
      <p>Dana Whitlow &ndash; President<br>4120 Larkspur Ridge Rd, Austin,<br>Texas 78700</p>
      <p class="phones"><strong>Cell: (512) 555-0148</strong><br>Fax: (512) 555-0172<br>Toll Free: (800) 555-0190</p>
      <p class="mail">dana@velnorecycling.com</p>
      <div class="socials"><i></i><i></i><i></i></div>
    </div>
  </footer>
  <div class="bottom-bar">
    <span>&copy;2018 Velno Recycling. All rights reserved.</span>
    <span class="bottom-links">Home &nbsp;|&nbsp; About &nbsp;|&nbsp; Contact Us</span>
    <span class="to-top"><svg width="8" height="8" viewBox="0 0 8 8" fill="#fff"><path d="M4 1l3 5H1z"/></svg></span>
  </div>

</div>
</body>
</html>
```